Business Card Design Project

I would like to have a project of business card with incorporated attachted logo elements in warm colors like: gold, yellow, brown.
We would like incorporate below information into the design
Name of the Company: Continental Hoop Invitational
Name: Dorian Pelkey
Position: Project Director
e-mail: dorian@hoopinvitational.net
mobile: +65 83147092
website: www.hoopinvitational.net
Address: 47 Marbury Lane, #06-11, Singapore 915274
There is a picture attachted which can be used as a back side of the buisness card - we would like to follow the colors theme on the front card ( with the person contact details) how ever the front card we will prefer with white background but with graphfic elements coming from logo.
Project Deadline Extended
Reason: the project has been launched on 24 of April with deadline by 24 of April by mistakes. Thats why I would like to extend the deadline.
Name: Dorian Pelkey
mobile: +65 83147092

```html
<!DOCTYPE html>
<html lang="en">
<head>
<meta charset="utf-8">
<title>Continental Hoop Invitational – Business Card</title>
<link rel="stylesheet" href="https://fonts.googleapis.com/css2?family=Mulish:wght@400;600;700;800&display=swap">
<style>
  :root {
    --page: #ecebe8;
    --card-white: #ffffff;
    --gold: #c39a2b;
    --gold-light: #e6b93a;
    --gold-deep: #c8961e;
    --ink: #1d1d1d;
    --divider: #e4e4e4;
    --violet: #7b3fb8;
    --charcoal: #262626;
  }
  * { box-sizing: border-box; margin: 0; padding: 0; }
  html, body {
    width: 1102px; height: 1200px; overflow: hidden;
    background: var(--page);
    font-family: "Mulish", "Helvetica Neue", Arial, sans-serif;
  }
  .canvas {
    position: relative; width: 1102px; height: 1200px;
  }
  .card {
    position: absolute; left: 101px; width: 900px; height: 514px;
    box-shadow: 0 6px 18px rgba(0,0,0,0.14);
  }
  /* Front */
  .card--front { top: 46px; background: var(--card-white); }
  .front-logo {
    position: absolute; left: 58px; top: 70px;
    display: flex; align-items: center; gap: 18px;
  }
  .front-logo__dot {
    width: 54px; height: 54px; border-radius: 50%;
    border: 6px solid var(--gold);
  }
  .front-logo__name {
    color: var(--gold); font-weight: 800; font-size: 30px;
    line-height: 1.05; text-transform: uppercase; letter-spacing: 0.5px;
  }
  .divider {
    position: absolute; left: 470px; top: 40px; width: 1px; height: 434px;
    background: var(--divider);
  }
  .holder {
    position: absolute; left: 58px; bottom: 74px;
  }
  .holder__marker {
    position: absolute; left: -58px; top: 10px;
    width: 0; height: 0;
    border-top: 11px solid transparent; border-bottom: 11px solid transparent;
    border-left: 16px solid var(--gold);
  }
  .holder__name {
    font-size: 30px; font-weight: 800; color: var(--ink); line-height: 1.15;
  }
  .holder__role {
    font-size: 17px; font-weight: 600; color: var(--gold); margin-top: 4px;
  }
  .contact {
    position: absolute; right: 40px; top: 150px;
    text-align: right; color: var(--ink);
    font-size: 21px; line-height: 1.25; font-weight: 600;
  }
  .contact__address { margin-bottom: 12px; padding-right: 38px; }
  .contact__line {
    display: flex; justify-content: flex-end; align-items: center; gap: 14px;
  }
  .icon {
    width: 22px; height: 22px; border-radius: 4px;
    background: var(--gold); display: inline-flex;
    align-items: center; justify-content: center; flex: none;
  }
  .icon svg { width: 14px; height: 14px; }
  /* Back */
  .card--back {
    top: 640px;
    background: linear-gradient(135deg, var(--gold-light) 0%, var(--gold-deep) 55%, #d9a92c 100%);
    display: flex; align-items: center; justify-content: center;
  }
  .back-logo {
    display: flex; align-items: center; gap: 24px;
  }
  .back-logo__dot {
    width: 84px; height: 84px; border-radius: 50%;
    background: var(--violet);
  }
  .back-logo__name {
    color: var(--charcoal); font-weight: 800; font-size: 44px;
    line-height: 1.05; text-transform: uppercase; letter-spacing: 0.5px;
  }
</style>
</head>
<body>
<main class="canvas">
  <section class="card card--front" aria-label="Business card front">
    <div class="front-logo">
      <span class="front-logo__dot"></span>
      <span class="front-logo__name">Continental Hoop<br>Invitational</span>
    </div>
    <div class="divider"></div>
    <div class="holder">
      <span class="holder__marker"></span>
      <p class="holder__name">Dorian Pelkey</p>
      <p class="holder__role">Project Director</p>
    </div>
    <address class="contact">
      <p class="contact__address">47 Marbury Lane, #06-11,<br>Singapore 915274</p>
      <p class="contact__line">+65 83147092
        <span class="icon"><svg viewBox="0 0 14 14"><rect x="4" y="1.5" width="6" height="11" rx="1.2" fill="none" stroke="#fff" stroke-width="1.4"/><circle cx="7" cy="10.5" r="0.8" fill="#fff"/></svg></span>
      </p>
      <p class="contact__line">dorian@hoopinvitational.net
        <span class="icon"><svg viewBox="0 0 14 14"><rect x="1.5" y="3" width="11" height="8" rx="1" fill="none" stroke="#fff" stroke-width="1.3"/><path d="M1.8 3.5 7 7.6l5.2-4.1" fill="none" stroke="#fff" stroke-width="1.3"/></svg></span>
      </p>
      <p class="contact__line">www.hoopinvitational.net
        <span class="icon"><svg viewBox="0 0 14 14"><circle cx="7" cy="7" r="5.3" fill="none" stroke="#fff" stroke-width="1.3"/><path d="M1.7 7h10.6M7 1.7c2.6 2.9 2.6 7.7 0 10.6M7 1.7c-2.6 2.9-2.6 7.7 0 10.6" fill="none" stroke="#fff" stroke-width="1.1"/></svg></span>
      </p>
    </address>
  </section>

  <section class="card card--back" role="img" aria-label="Business card back: brushed gold texture with the event name">
    <div class="back-logo">
      <span class="back-logo__dot"></span>
      <span class="back-logo__name">Continental Hoop<br>Invitational</span>
    </div>
  </section>
</main>
</body>
</html>
```